Website Landing Page for Brightfall Systems

Create a custom designed website landing page for our business. Looking for a professional upscale design that incorporates our logo and logo colors into the theme. I want a standard fixed frame website, not a constant scrolling format that seems to be the trend. To start with I'm looking for more of the graphic design part, maybe a concept or theme, I don't expect to see a finished project. Not interested in generic templates or layouts.

The name of our company is Brightfall Systems and I've attached our logo below. I'd like to have the web page have the same look and feel of our logo, as well as the colors. Our company, Brightfall Systems does system design, installation, and programming, of residential and commercial Audio/Video and Automation systems. We do home theaters, lighting and building automation, video conferencing systems, security camera installations, conference rooms, projectors, distributed audio systems, and similar Technology projects. This will be a professional services/informational website. We will not sell products on this website. This website will be used to advertise our company and communicate our services to prospective customers. Having a well designed, professional and clean website is one way we want to distinguish our company from the competition.

Here are some examples of what I consider a professional well designed website
http://www.qorlamstudio.com/Work/

Last year we had our tradlo store designed (with PixelMarket) and I'm really happy with the way it turned out. You can see it at www.HolvenGearDepot.com I consider this to be a great design and looking for the same level of quality with this new website. However, do not copy or use any part of this design in this new project. This tradlo store is completely separate from our other company Brightfall Systems. I only mention this tradlo store an an example of good work.

Reason: Still going through designs.

Reason: Still working on project and have not had time to review all designs and request revisions.

Reason: Sill going through designs and requesting revisions

Reason: still going through all the submissions we received.

Target Market(s)

People interested in Audio/Video, home theaters, home automation. We do sales, system design, and programming. We typically work on larger projects with both residential and commercial customers.

Industry/Entity Type

Business

Number of Pages Required

1 page

Requirements
Must have
• Great design elements. Please use a white background. I think white goes well with our logo colors.

```html
<!DOCTYPE html>
<html lang="en">
<head>
<meta charset="utf-8">
<title>Brightfall Systems</title>
<link href="https://fonts.googleapis.com/css2?family=Questrial&family=Archivo+Narrow:wght@400;600&display=swap" rel="stylesheet">
<style>
:root{
  --white:#ffffff;
  --ink:#2b2b2b;
  --dark:#2f2f2f;
  --blue:#2a9fd8;
  --green:#5cb833;
  --gray-panel:#f2f2f2;
  --muted:#7a7a7a;
  --line:#cfcfcf;
}
*{margin:0;padding:0;box-sizing:border-box}
html,body{width:901px;height:1200px;overflow:hidden;background:var(--white)}
body{font-family:"Questrial",sans-serif;color:var(--ink)}
.page{position:relative;width:901px;height:1200px;overflow:hidden}
.topbar{position:absolute;left:0;top:0;width:901px;height:22px;
  background:repeating-linear-gradient(45deg,#3d3d3d 0 2px,#333 2px 4px);
  color:var(--white);font-size:9px;display:flex;align-items:center;justify-content:flex-end;padding-right:18px;gap:8px}
.topbar .phone{display:flex;align-items:center;gap:5px}
.header{position:absolute;left:0;top:22px;width:901px;height:94px}
.brand{position:absolute;left:85px;top:17px;display:flex;align-items:center;gap:10px}
.brand-mark{width:48px;height:48px;border-radius:50%;border:4px solid var(--blue)}
.brand-name{font-family:"Archivo Narrow",sans-serif;font-weight:600;font-size:15px;line-height:15px;color:var(--blue);letter-spacing:.5px;text-transform:uppercase}
.nav{position:absolute;left:414px;top:36px;display:flex;font-family:"Archivo Narrow",sans-serif;font-weight:400;font-size:9px;letter-spacing:.2px}
.nav a{color:var(--ink);text-decoration:none}
.nav .i1{width:135px}.nav .i2{width:67px}.nav .i3{width:56px}
.search{position:absolute;left:753px;top:30px;width:64px;height:24px;border:1px solid var(--line);border-radius:12px 0 0 12px;font-size:8px;color:#b5b5b5;padding:7px 0 0 13px}
.search svg{position:absolute;right:5px;top:7px}
.hero{position:absolute;left:85px;top:116px;width:731px;height:334px;
  background:linear-gradient(180deg,#1f4f82 0%,#143a66 45%,#0d2748 100%)}
.hero .scene{position:absolute;inset:0;background:radial-gradient(ellipse at 50% 40%,rgba(70,130,190,.55),transparent 65%)}
.hero h1{position:absolute;left:0;width:100%;top:116px;text-align:center;color:var(--white);font-weight:400;font-size:29px;letter-spacing:-.3px}
.hero .watch{position:absolute;left:285px;top:173px;color:var(--white);font-family:"Archivo Narrow",sans-serif;font-size:11px;line-height:15px;font-weight:600}
.hero .play{position:absolute;left:390px;top:169px}
.hero .arrow{position:absolute;top:155px}
.dots{position:absolute;display:flex;gap:6px}
.dots span{width:6px;height:6px;border-radius:50%;background:rgba(255,255,255,.4)}
.dots span.on{background:var(--white)}
.tile{position:absolute;top:474px;width:358px;height:144px;display:flex;align-items:center;justify-content:center;color:var(--white);font-size:19px;letter-spacing:.2px}
.tile.residential{left:85px;background:linear-gradient(135deg,#3e8a1e,#5cb833 55%,#2f7440)}
.tile.commercial{left:458px;background:linear-gradient(135deg,#4fae28,#2d8d5a 60%,#1e6a86)}
.tile.commercial span{border-bottom:2px solid var(--white);padding-bottom:2px}
.services{position:absolute;left:86px;top:640px;width:730px;height:161px;display:flex;
  background:linear-gradient(90deg,#4aa83a 0%,#3fa36a 40%,#2f92b2 70%,#2384cc 100%)}
.service{position:relative;border-right:1px solid rgba(255,255,255,.25);color:var(--white);text-align:center;font-size:10.5px;line-height:15px;text-transform:uppercase}
.service:last-child{border-right:0}
.service .icon{position:absolute;left:50%;top:26px;transform:translateX(-50%)}
.service .label{position:absolute;left:0;width:100%}
.btn{position:absolute;left:50%;transform:translateX(-50%);width:75px;height:18px;border:1px solid var(--white);border-radius:9px;font-size:7.5px;line-height:16px;color:var(--white)}
.round-arrow{position:absolute;width:26px;height:26px;border-radius:50%;background:var(--white);box-shadow:0 1px 4px rgba(0,0,0,.2);display:flex;align-items:center;justify-content:center}
.testimonial{position:absolute;left:84px;top:825px;width:732px;height:133px;background:var(--gray-panel)}
.quote-mark{position:absolute;left:151px;top:20px;font-size:22px;color:var(--ink);font-family:Georgia,serif}
.quote{position:absolute;left:168px;top:34px;width:248px;font-size:9.5px;line-height:13px}
.cite{position:absolute;left:190px;top:69px;width:237px;text-align:right;font-size:7.5px;font-style:italic;color:var(--muted)}
.avatar{position:absolute;left:449px;top:33px;width:48px;height:48px;border-radius:50%;background:linear-gradient(135deg,#e6b79a,#a8603e)}
.footer{position:absolute;left:0;top:981px;width:901px;height:219px;background:var(--dark);color:var(--white);font-size:8.5px;line-height:15px}
.fcol{position:absolute;top:35px}
.fcol h3{font-size:10.5px;letter-spacing:.3px;margin-bottom:14px;font-weight:700}
.fcol p{text-transform:uppercase}
.fcol .gap{margin-top:11px}
.fcol .strong{font-weight:700}
.signup{display:flex;margin-top:20px;width:133px;height:26px}
.signup .field{flex:1;background:var(--white);display:flex;align-items:center;gap:8px;padding-left:10px;color:#aaa;font-size:7.5px;text-transform:none}
.signup .go{width:33px;background:var(--blue);display:flex;align-items:center;justify-content:center}
.social{display:flex;gap:15px;margin-top:8px;padding-left:1px}
.social span{width:10px;height:10px;border-radius:50%;background:var(--white)}
.copyright{position:absolute;left:0;width:100%;top:196px;text-align:center;font-family:"Archivo Narrow",sans-serif;font-size:8.5px}
</style>
</head>
<body>
<div class="page">
  <div class="topbar">
    <span class="phone">
      <svg width="10" height="10" viewBox="0 0 10 10"><circle cx="5" cy="5" r="5" fill="#fff"/><path d="M3.3 2.6l1 1-.5.6c.3.6.8 1.1 1.4 1.4l.6-.5 1 1-.7.8c-1.6-.4-2.7-1.5-3.1-3.1z" fill="#333"/></svg>
      (555) 214-7730
    </span>
    <span>Talk with an Expert</span>
  </div>

  <header class="header">
    <div class="brand">
      <div class="brand-mark"></div>
      <div class="brand-name">Brightfall<br>Systems</div>
    </div>
    <nav class="nav">
      <a class="i1" href="#">HOME &amp; COMMERCIAL AV</a>
      <a class="i2" href="#">PORTFOLIO</a>
      <a class="i3" href="#">ABOUT</a>
      <a href="#">SUPPORT</a>
    </nav>
    <div class="search">Search
      <svg width="9" height="9" viewBox="0 0 9 9"><circle cx="3.7" cy="3.7" r="2.8" fill="none" stroke="#999" stroke-width="1.2"/><path d="M5.8 5.8l2.5 2.5" stroke="#999" stroke-width="1.2"/></svg>
    </div>
  </header>

  <section class="hero">
    <div class="scene" role="img" aria-label="Modern conference room with a long table, black chairs and a wall display, tinted blue"></div>
    <h1>YOUR SOURCE FOR SMART SOLUTION</h1>
    <div class="watch">WHAT WE DO?<br>Watch OVERVIEW</div>
    <svg class="play" width="38" height="38" viewBox="0 0 38 38"><circle cx="19" cy="19" r="17.5" fill="none" stroke="#fff" stroke-width="2"/><path d="M16 14l8 5-8 5z" fill="#fff"/></svg>
    <svg class="arrow" style="left:19px" width="26" height="26" viewBox="0 0 26 26"><circle cx="13" cy="13" r="12" fill="none" stroke="rgba(255,255,255,.5)" stroke-width="1.5"/><path d="M15 8l-5 5 5 5" fill="none" stroke="rgba(255,255,255,.6)" stroke-width="1.5"/></svg>
    <svg class="arrow" style="left:686px" width="26" height="26" viewBox="0 0 26 26"><circle cx="13" cy="13" r="12" fill="none" stroke="rgba(255,255,255,.7)" stroke-width="1.5"/><path d="M11 8l5 5-5 5" fill="none" stroke="#fff" stroke-width="1.5"/></svg>
    <div class="dots" style="left:640px;top:321px"><span class="on"></span><span></span><span></span><span></span><span></span><span></span></div>
  </section>

  <a class="tile residential" role="img" aria-label="Green tinted living room with a wall display"><span>RESIDENTIAL AV</span></a>
  <a class="tile commercial" role="img" aria-label="Green tinted auditorium seating"><span>COMMERCIAL AV</span></a>

  <section class="services">
    <div class="service" style="width:116px">
      <svg class="icon" width="40" height="26" viewBox="0 0 40 26" fill="none" stroke="#fff" stroke-width="1.2" opacity=".8"><rect x="1" y="2" width="6" height="22"/><rect x="33" y="2" width="6" height="22"/><rect x="10" y="8" width="20" height="14"/><circle cx="16" cy="15" r="2"/><circle cx="24" cy="15" r="2"/></svg>
      <div class="label" style="top:76px">Home Theaters</div>
      <div class="btn" style="top:109px">LEARN MORE</div>
    </div>
    <div class="service" style="width:125px">
      <svg class="icon" width="40" height="30" viewBox="0 0 40 30" fill="none" stroke="#fff" stroke-width="1.2" opacity=".8"><path d="M6 8l14 6-6 10-10-8z"/><path d="M22 14l6-4M23 18l7 1M20 22l4 5"/></svg>
      <div class="label" style="top:76px">Lighting and<br>Building<br>Automation</div>
      <div class="btn" style="top:130px">LEARN MORE</div>
    </div>
    <div class="service" style="width:125px">
      <svg class="icon" width="40" height="30" viewBox="0 0 40 30" fill="none" stroke="#fff" stroke-width="1.2" opacity=".8"><rect x="3" y="2" width="14" height="10"/><rect x="23" y="2" width="14" height="10"/><circle cx="20" cy="18" r="5"/><path d="M20 23v5M14 28h12"/></svg>
      <div class="label" style="top:76px">Video<br>Conferencing<br>Systems</div>
      <div class="btn" style="top:130px;left:65px">LEARN MORE</div>
    </div>
    <div class="service" style="width:125px">
      <svg class="icon" width="40" height="36" viewBox="0 0 40 36" fill="none" stroke="#fff" stroke-width="1.2" opacity=".8"><path d="M10 6l26 10-5 8-24-11z"/><path d="M12 20v10M4 30h8v-8H4z"/></svg>
      <div class="label" style="top:76px">Security Camera<br>Installations</div>
      <div class="btn" style="top:120px">LEARN MORE</div>
    </div>
    <div class="service" style="width:125px">
      <svg class="icon" width="40" height="40" viewBox="0 0 40 40" fill="none" stroke="#fff" stroke-width="1.2" opacity=".8"><circle cx="20" cy="20" r="18"/><rect x="17" y="12" width="6" height="16"/><path d="M20 6v4M20 30v4"/></svg>
      <div class="label" style="top:76px">Conference<br>Rooms</div>
      <div class="btn" style="top:120px">LEARN MORE</div>
    </div>
    <div class="service" style="width:114px">
      <svg class="icon" width="36" height="20" viewBox="0 0 36 20" fill="none" stroke="#fff" stroke-width="1.5" opacity=".8"><rect x="2" y="4" width="30" height="12" rx="3"/><circle cx="11" cy="10" r="3.5"/><path d="M19 8h9M19 12h9"/></svg>
      <div class="label" style="top:86px">Projectors</div>
      <div class="btn" style="top:109px">LEARN MORE</div>
    </div>
  </section>
  <div class="round-arrow" style="left:68px;top:708px"><svg width="10" height="10" viewBox="0 0 10 10"><path d="M6.5 1.5L3 5l3.5 3.5" fill="none" stroke="var(--blue)" stroke-width="1.8"/></svg></div>
  <div class="round-arrow" style="left:807px;top:708px"><svg width="10" height="10" viewBox="0 0 10 10"><path d="M3.5 1.5L7 5 3.5 8.5" fill="none" stroke="var(--blue)" stroke-width="1.8"/></svg></div>

  <section class="testimonial">
    <div class="quote-mark">&ldquo;</div>
    <p class="quote">Brightfall Systems is my number one choice for my customers, and my own home.</p>
    <p class="cite">Mara Ellison, Interior Decorator, Ashford, KY</p>
    <div class="avatar" role="img" aria-label="Portrait of the client quoted"></div>
    <div class="round-arrow" style="left:545px;top:29px"><svg width="10" height="10" viewBox="0 0 10 10"><path d="M6.5 1.5L3 5l3.5 3.5" fill="none" stroke="#222" stroke-width="1.8"/></svg></div>
    <div class="round-arrow" style="left:545px;top:57px"><svg width="10" height="10" viewBox="0 0 10 10"><path d="M3.5 1.5L7 5 3.5 8.5" fill="none" stroke="#222" stroke-width="1.8"/></svg></div>
    <div class="dots" style="left:442px;top:103px"><span style="background:#cfcfcf"></span><span style="background:#cfcfcf"></span><span style="background:#cfcfcf"></span><span style="background:#222"></span><span style="background:#cfcfcf"></span><span style="background:#cfcfcf"></span></div>
  </section>

  <footer class="footer">
    <div class="fcol" style="left:84px">
      <h3>BRIGHTFALL SYSTEMS</h3>
      <p>AV System Design Company</p>
      <p class="gap">1840 Lindow Avenue</p>
      <p>Cedar Hollow, TX 75990</p>
      <p class="strong">Toll Free: (555) 214-7730</p>
      <p>Local: (555) 318-4402</p>
      <p>Fax: (555) 318-4490</p>
    </div>
    <div class="fcol" style="left:301px">
      <h3>STORE HOURS</h3>
      <p>Mon - Fri: 10 - 8 PM</p>
      <p>Sunday: Closed</p>
    </div>
    <div class="fcol" style="left:481px">
      <h3>QUICK LINKS</h3>
      <p>Ask an Expert</p>
      <p>About Us</p>
      <p>Help Center</p>
      <p>Shipping &amp; Delivery Info</p>
      <p>Return Policy</p>
      <p>Our Story</p>
      <p>Meet the Staff</p>
    </div>
    <div class="fcol" style="left:659px">
      <h3>CONNECT WITH US</h3>
      <p>Join our email list for<br>special offers:</p>
      <div class="signup">
        <div class="field"><svg width="11" height="8" viewBox="0 0 11 8"><rect width="11" height="8" fill="var(--blue)"/><path d="M0 0l5.5 4L11 0" fill="none" stroke="#fff" stroke-width="1"/></svg>Your email..</div>
        <div class="go"><svg width="10" height="8" viewBox="0 0 10 8"><path d="M1 4l3 3 5-6" fill="none" stroke="#fff" stroke-width="1.8"/></svg></div>
      </div>
      <p style="margin-top:12px">Social Medias</p>
      <div class="social"><span></span><span></span><span></span><span></span><span></span></div>
    </div>
    <p class="copyright">Copyright &copy; 2017 Brightfall Systems. All Rights Reserved.</p>
  </footer>
</div>
</body>
</html>
```